Build me a powerpoint template for my brand A cycle label named Varo.

Our project is to create marketing materials for raising investment into our biking wellness brand called a cycle label named Varo. Our brand is built around wellness and healthy living through biking in the black community. Please see a link to our active instagram account for inspiration.

https://www.instagram.com/acyclelabelnamedvaro/

```html
<!DOCTYPE html>
<html lang="en">
<head>
<meta charset="utf-8">
<title>Velomara Presentation Template</title>
<link href="https://fonts.googleapis.com/css2?family=Montserrat:ital,wght@0,600;0,800;1,800&family=Open+Sans:wght@400;600&display=swap" rel="stylesheet">
<style>
  :root{
    --canvas:#d9d6d3;
    --ink:#1f1f1f;
    --lime:#86e01e;
    --orange:#e2551f;
    --paper:#ffffff;
    --muted:#b9b9b9;
  }
  *{box-sizing:border-box;margin:0;padding:0}
  html,body{width:1200px;height:675px;overflow:hidden;background:var(--canvas)}
  .deck{
    width:1200px;height:675px;padding:57px 20px 0 21px;
    display:grid;grid-template-columns:repeat(4,280px);grid-auto-rows:158px;
    gap:16px 13px;
  }
  .slide{position:relative;width:280px;height:158px;background:var(--ink);overflow:hidden}
  .abs{position:absolute}
  .photo{position:absolute}
  .photo--warm{background:linear-gradient(135deg,#7a3b2e,#b0624a 55%,#3d2a25)}
  .photo--street{background:linear-gradient(160deg,#8a7a6c,#4b4039 60%,#2a2421)}
  .photo--park{background:linear-gradient(160deg,#6f7d5c,#3f4a35 60%,#262b22)}
  .photo--bright{background:linear-gradient(160deg,#c9c4bc,#8c8880 60%,#55524d)}
  .photo--mono{background:linear-gradient(160deg,#e4e4e4,#9a9a9a 60%,#4a4a4a)}
  .photo--night{background:linear-gradient(180deg,#2f3d2c,#1b241a)}
  .block-lime{position:absolute;background:var(--lime)}
  .block-orange{position:absolute;background:var(--orange)}
  .title{
    position:absolute;font-family:'Montserrat',sans-serif;font-weight:800;font-style:italic;
    text-transform:uppercase;color:var(--paper);font-size:8px;line-height:1.15;letter-spacing:.2px;white-space:nowrap
  }
  .title .lime{color:var(--lime)}
  .title .orange{color:var(--orange)}
  .kicker{position:absolute;font-family:'Open Sans',sans-serif;font-weight:600;font-size:4px;color:var(--orange);white-space:nowrap}
  .kicker--lime{color:var(--lime)}
  .body{position:absolute;font-family:'Open Sans',sans-serif;font-size:3.6px;line-height:1.5;color:var(--muted)}
  .btn{
    position:absolute;font-family:'Montserrat',sans-serif;font-weight:600;font-size:3.4px;
    text-transform:uppercase;padding:2px 5px;white-space:nowrap
  }
  .btn--orange{background:var(--orange);color:var(--paper)}
  .btn--white{background:var(--paper);color:var(--ink)}
  .square{position:absolute;width:9px;height:9px;background:var(--lime)}
  .num{
    position:absolute;width:7px;height:7px;background:var(--orange);color:var(--paper);
    font-family:'Montserrat',sans-serif;font-weight:800;font-size:3.2px;display:flex;align-items:center;justify-content:center
  }
  .ring-label{position:absolute;font-family:'Open Sans',sans-serif;font-size:3px;color:var(--muted);text-align:center;width:20px}
  .brand{
    position:absolute;display:flex;align-items:center;gap:4px;
    font-family:'Montserrat',sans-serif;font-weight:800;font-size:17px;color:var(--paper);letter-spacing:.5px
  }
  .brand__dot{width:9px;height:9px;border-radius:50%;background:var(--paper)}
  .contact-card{position:absolute;background:var(--paper);display:grid;grid-template-columns:repeat(3,1fr);gap:6px 6px;padding:9px 10px;align-content:start}
  .contact-card dt{font-family:'Open Sans',sans-serif;font-weight:600;font-size:3.2px;color:var(--ink)}
  .contact-card dd{font-family:'Open Sans',sans-serif;font-size:3px;color:#666}
  .panel-white{position:absolute;background:var(--paper)}
</style>
</head>
<body>
<main class="deck">

  <section class="slide slide--cover">
    <div class="photo photo--warm" style="inset:0" role="img" aria-label="Rider standing by a brick doorway"></div>
    <p class="kicker kicker--lime" style="left:15px;top:16px;font-size:4.5px">Portfolio Presentation</p>
    <p class="body" style="left:15px;top:23px;color:#eee;font-size:3.2px">www.velomararides.com</p>
    <div class="brand" style="left:80px;top:90px"><span class="brand__dot"></span>VELOMARA</div>
  </section>

  <section class="slide">
    <h2 class="title" style="left:28px;top:34px">Welcome to<br><span class="lime">Our Store</span></h2>
    <p class="kicker" style="left:28px;top:56px">Description Here</p>
    <p class="body" style="left:28px;top:66px;width:105px">Velomara rides with purpose. We build gear and routes that help our community move, heal and grow stronger together.</p>
    <p class="body" style="left:28px;top:98px;width:105px">Every ride is a step toward better health.</p>
    <div class="block-lime" style="left:143px;top:0;width:17px;height:53px"></div>
    <div class="photo photo--warm" style="left:155px;top:34px;width:118px;height:106px" role="img" aria-label="Rider at a red doorway"></div>
  </section>

  <section class="slide">
    <div class="photo photo--street" style="left:0;top:22px;width:50px;height:100px" role="img" aria-label="Rider holding a branded bag"></div>
    <div class="photo photo--mono" style="left:48px;top:30px;width:48px;height:96px" role="img" aria-label="Rider in denim"></div>
    <div class="photo photo--bright" style="left:96px;top:0;width:44px;height:90px" role="img" aria-label="Rider in a white tee"></div>
    <div class="photo photo--mono" style="left:84px;top:100px;width:14px;height:22px" role="img" aria-label="Street detail"></div>
    <h2 class="title" style="left:164px;top:44px">Overview Fashion</h2>
    <p class="kicker kicker--lime" style="left:164px;top:55px">Description Text</p>
    <svg class="abs" style="left:164px;top:98px" width="80" height="16" viewBox="0 0 80 16" aria-hidden="true">
      <g fill="none" stroke-width="2"><circle cx="8" cy="8" r="6" stroke="#444"/><circle cx="8" cy="8" r="6" stroke="#86e01e" stroke-dasharray="28 40" transform="rotate(-90 8 8)"/>
      <circle cx="32" cy="8" r="6" stroke="#444"/><circle cx="32" cy="8" r="6" stroke="#86e01e" stroke-dasharray="32 40" transform="rotate(-90 32 8)"/>
      <circle cx="56" cy="8" r="6" stroke="#444"/><circle cx="56" cy="8" r="6" stroke="#86e01e" stroke-dasharray="24 40" transform="rotate(-90 56 8)"/></g>
    </svg>
    <p class="ring-label" style="left:162px;top:116px">Comfort</p>
    <p class="ring-label" style="left:186px;top:116px">Style</p>
    <p class="ring-label" style="left:210px;top:116px">Durable</p>
  </section>

  <section class="slide">
    <div class="block-lime" style="left:131px;top:0;width:12px;height:48px"></div>
    <div class="photo photo--street" style="left:141px;top:0;width:139px;height:79px" role="img" aria-label="Riders resting beside bikes"></div>
    <h2 class="title" style="left:30px;top:40px">We use the<br>best clothing<br><span class="orange">Materials</span></h2>
    <div class="square" style="left:30px;top:100px"></div>
    <p class="body" style="left:42px;top:100px;width:38px">Breathable fabric made for long rides.</p>
    <div class="square" style="left:108px;top:100px"></div>
    <p class="body" style="left:120px;top:100px;width:38px">Breathable fabric made for long rides.</p>
    <div class="square" style="left:186px;top:100px"></div>
    <p class="body" style="left:198px;top:100px;width:38px">Breathable fabric made for long rides.</p>
  </section>

  <section class="slide">
    <h2 class="title" style="left:28px;top:30px">Our<br><span class="lime">Advantages</span></h2>
    <p class="body" style="left:128px;top:28px;width:72px">Quality gear, local rides and a community that keeps you moving.</p>
    <span class="btn btn--orange" style="left:128px;top:58px">Learn More</span>
    <div class="block-orange" style="left:210px;top:32px;width:20px;height:40px"></div>
    <div class="photo photo--street" style="left:231px;top:0;width:49px;height:63px" role="img" aria-label="Rider on a city street"></div>
    <div class="block-orange" style="left:49px;top:72px;width:20px;height:50px"></div>
    <div class="photo photo--mono" style="left:0;top:79px;width:56px;height:79px" role="img" aria-label="Branded backpack"></div>
    <p class="kicker" style="left:85px;top:93px">Advantage 01</p>
    <p class="body" style="left:85px;top:100px;width:44px">Built for comfort on every road.</p>
    <p class="kicker" style="left:141px;top:93px">Advantage 02</p>
    <p class="body" style="left:141px;top:100px;width:44px">Built for comfort on every road.</p>
    <p class="kicker" style="left:198px;top:93px">Advantage 03</p>
    <p class="body" style="left:198px;top:100px;width:44px">Built for comfort on every road.</p>
  </section>

  <section class="slide">
    <h2 class="title" style="left:0;right:0;top:24px;text-align:center;font-size:13px">Fashion Gallery</h2>
    <div class="block-lime" style="left:4px;top:72px;width:14px;height:50px"></div>
    <div class="photo photo--night" style="left:18px;top:53px;width:58px;height:89px" role="img" aria-label="Rider in a black hoodie"></div>
    <div class="photo photo--street" style="left:78px;top:53px;width:28px;height:43px" role="img" aria-label="Street corner"></div>
    <div class="photo photo--park" style="left:78px;top:98px;width:28px;height:44px" role="img" aria-label="Trees along a path"></div>
    <div class="photo photo--warm" style="left:108px;top:53px;width:85px;height:89px" role="img" aria-label="Rider seated in an alley"></div>
    <div class="photo photo--street" style="left:195px;top:53px;width:58px;height:89px" role="img" aria-label="Rider in a brick alley"></div>
    <div class="block-lime" style="left:253px;top:72px;width:14px;height:50px"></div>
  </section>

  <section class="slide">
    <div class="block-lime" style="left:0;top:47px;width:23px;height:111px"></div>
    <div class="block-lime" style="left:0;top:129px;width:111px;height:29px"></div>
    <div class="photo photo--warm" style="left:23px;top:0;width:88px;height:129px" role="img" aria-label="Founder seated in an alley"></div>
    <div class="block-lime" style="left:124px;top:0;width:19px;height:52px"></div>
    <p class="kicker" style="left:164px;top:34px">Founder Profile</p>
    <h2 class="title" style="left:164px;top:41px;font-size:10px;color:var(--orange)">Dayo Renfield</h2>
    <svg class="abs" style="left:164px;top:66px" width="80" height="12" viewBox="0 0 80 12" aria-hidden="true">
      <g fill="none" stroke-width="2"><path d="M2 10a8 8 0 0 1 16 0" stroke="#444"/><path d="M2 10a8 8 0 0 1 14 -5" stroke="#86e01e"/>
      <path d="M26 10a8 8 0 0 1 16 0" stroke="#444"/><path d="M26 10a8 8 0 0 1 15 -3" stroke="#86e01e"/>
      <path d="M50 10a8 8 0 0 1 16 0" stroke="#444"/><path d="M50 10a8 8 0 0 1 12 -7" stroke="#86e01e"/></g>
    </svg>
    <p class="ring-label" style="left:164px;top:80px">Vision</p>
    <p class="ring-label" style="left:188px;top:80px">Drive</p>
    <p class="ring-label" style="left:212px;top:80px">Focus</p>
    <p class="body" style="left:164px;top:89px;width:84px">Founder and lifelong rider leading Velomara with heart.</p>
    <span class="btn btn--white" style="left:164px;top:112px">More Profile</span>
  </section>

  <section class="slide">
    <svg class="abs" style="left:35px;top:22px" width="118" height="98" viewBox="0 0 150 125" aria-label="Bar chart of yearly sales">
      <g stroke="#3a3a3a" stroke-width=".5"><line x1="0" y1="20" x2="150" y2="20"/><line x1="0" y1="45" x2="150" y2="45"/><line x1="0" y1="70" x2="150" y2="70"/><line x1="0" y1="95" x2="150" y2="95"/><line x1="0" y1="120" x2="150" y2="120"/></g>
      <g fill="#cfcfcf"><rect x="12" y="96" width="8" height="24"/><rect x="36" y="88" width="8" height="32"/><rect x="60" y="92" width="8" height="28"/><rect x="84" y="70" width="8" height="50"/><rect x="108" y="76" width="8" height="44"/><rect x="132" y="66" width="8" height="54"/></g>
      <g fill="#86e01e"><rect x="21" y="100" width="8" height="20"/><rect x="45" y="80" width="8" height="40"/><rect x="69" y="58" width="8" height="62"/><rect x="93" y="84" width="8" height="36"/><rect x="117" y="26" width="8" height="94"/></g>
      <g fill="#9a9a9a" font-family="Open Sans, sans-serif" font-size="4"><text x="14" y="126">2018</text><text x="38" y="126">2019</text><text x="62" y="126">2020</text><text x="86" y="126">2021</text><text x="110" y="126">2022</text></g>
    </svg>
    <h2 class="title" style="left:172px;top:34px">Our Sales<br><span class="orange">Statistics</span></h2>
    <p class="body" style="left:172px;top:54px;width:80px">Sales grew each year as our riding community expanded.</p>
    <div class="block-lime" style="left:274px;top:118px;width:6px;height:12px"></div>
  </section>

  <section class="slide">
    <h2 class="title" style="left:28px;top:38px">Store Mission</h2>
    <div class="square" style="left:28px;top:60px"></div>
    <p class="body" style="left:42px;top:60px;width:80px">We get more people riding for health and joy.</p>
    <div class="square" style="left:28px;top:100px"></div>
    <p class="body" style="left:42px;top:100px;width:80px">We get more people riding for health and joy.</p>
    <div class="photo photo--park" style="left:152px;top:0;width:62px;height:158px" role="img" aria-label="Riders resting in a park"></div>
    <div class="photo photo--bright" style="left:215px;top:0;width:65px;height:158px" role="img" aria-label="Rider on a bike in the street"></div>
    <div class="block-lime" style="left:144px;top:0;width:17px;height:51px"></div>
  </section>

  <section class="slide">
    <div class="photo photo--bright" style="left:0;top:0;width:96px;height:158px" role="img" aria-label="Rider with a bike on a city sidewalk"></div>
    <div class="block-lime" style="left:90px;top:0;width:17px;height:51px"></div>
    <div class="panel-white" style="left:0;top:117px;width:96px;height:41px"></div>
    <h2 class="title" style="left:8px;top:134px;color:var(--ink);font-size:8px">Keep Riding</h2>
    <h2 class="title" style="left:132px;top:36px">Store Vision</h2>
    <div class="num" style="left:132px;top:58px">01</div><p class="body" style="left:144px;top:58px;width:96px">Open rides in every neighborhood we serve.</p>
    <div class="num" style="left:132px;top:78px">02</div><p class="body" style="left:144px;top:78px;width:96px">Open rides in every neighborhood we serve.</p>
    <div class="num" style="left:132px;top:98px">03</div><p class="body" style="left:144px;top:98px;width:96px">Open rides in every neighborhood we serve.</p>
    <div class="num" style="left:132px;top:118px">04</div><p class="body" style="left:144px;top:118px;width:96px">Open rides in every neighborhood we serve.</p>
  </section>

  <section class="slide">
    <h2 class="title" style="left:0;right:0;top:30px;text-align:center">Velomara Contact</h2>
    <div class="photo photo--night" style="left:0;top:83px;width:280px;height:75px" role="img" aria-label="Rider framed by trees"></div>
    <dl class="contact-card" style="left:46px;top:50px;width:185px;height:62px">
      <div><dt>Description</dt><dd>Cycle wellness label</dd></div>
      <div><dt>Email</dt><dd>hello@velomararides.com</dd></div>
      <div><dt>Social Media</dt><dd>@velomara.rides</dd></div>
      <div><dt>Telephone</dt><dd>+1 555 0142</dd></div>
      <div><dt>Website</dt><dd>velomararides.com</dd></div>
      <div><dt>Office Address</dt><dd>120 Cadence Ave</dd></div>
    </dl>
  </section>

  <section class="slide">
    <h2 class="title" style="left:30px;top:34px;font-size:20px;line-height:1.05">Thank<br><span class="lime">You</span></h2>
    <p class="body" style="left:30px;top:100px;width:100px">Thanks for riding with us. Let's build a healthier future together.</p>
    <div class="panel-white" style="left:170px;top:0;width:110px;height:158px"></div>
    <div class="photo photo--mono" style="left:188px;top:20px;width:72px;height:118px" role="img" aria-label="Black and white portrait of a rider"></div>
  </section>

</main>
</body>
</html>
```